harbor lantern security & electric needs a business card

Must be attractive and modern, look professional and upscale!!
We provide alarm and cameras services and 24 hour monitoring for commercial and residential clients. In addition, the owner is a master electrician that provides services to commercial and residential clients.
We also install and service automatic gates. We previously had two different businesses but decided to merge into one, thus creating Harbor Lantern Security & Electric.

Target Market(s)

Commercial Business and residential customers

Industry/Entity Type

Security

Contact Information for Business Card

Front and back design with logo and services listed

Font styles to use
Sans Serif

Colors
ec1f27
0355a3
fbee3f

Requirements
Must have
• Front of card:
• Marcus Tremblow-Owner
• telephone icon and then the number 936-555-0193
• Mail icon and then email address mtremblow@quillmail.example
• World Icon then website www.yourharborlanterntx.example
• Location marker and then Marrowdale, Texas
• We would like to have a picture of the logo at least on the front
• Also need motto on front: We're There When You're Not
• The front of the card must also say Licensed and Insured in addition to:
• License Number: K47315
• TECL: 58629
• On the Back of the Card:
• List each of these Services with check marks:
• Residential and Commercial Electrical Services
• Electric Gates
• Alarm Systems
• Alarm Monitoring
• Cameras
• ***Use separate attached logo, the business card design is just to be used as a model***
Nice to have
• It would be nice to have the logo on back of the card in addition to these words at the bottom:
• "No job too big or small, we do it all!"
Should not have
• Anything crazy!!

```html
<!DOCTYPE html>
<html lang="en">
<head>
<meta charset="utf-8">
<title>Harbor Lantern Security &amp; Electric – Business Card</title>
<link rel="stylesheet" href="https://fonts.googleapis.com/css2?family=Source+Sans+3:wght@400;600;700&display=swap">
<style>
  :root {
    --red: #e21f26;
    --navy: #1f3a6e;
    --rule: #9aa3b8;
    --rule-red: #e88a8e;
    --card: #ffffff;
    --bg-top: #2a2a2a;
    --bg-bottom: #050505;
  }
  * { margin: 0; padding: 0; box-sizing: border-box; }
  html, body { width: 1200px; height: 900px; overflow: hidden; }
  body {
    position: relative;
    background: linear-gradient(180deg, var(--bg-top) 0%, #141414 55%, var(--bg-bottom) 100%);
    font-family: "Source Sans 3", "Myriad Pro", Arial, sans-serif;
    color: var(--navy);
  }
  .card {
    position: absolute;
    top: 306px;
    height: 271px;
    background: var(--card);
    border-radius: 12px;
    box-shadow: 0 6px 18px rgba(0,0,0,0.45);
    overflow: hidden;
  }
  .card--front { left: 149px; width: 439px; }
  .card--back { left: 608px; width: 441px; }

  /* brand mark stand-in */
  .brand {
    position: absolute;
    display: flex;
    flex-direction: column;
    align-items: center;
    text-align: center;
    color: var(--navy);
    font-weight: 700;
  }
  .brand__dot { border-radius: 50%; background: var(--red); }
  .card--front .brand { left: 30px; top: 62px; width: 170px; font-size: 19px; line-height: 1.15; gap: 12px; }
  .card--front .brand__dot { width: 46px; height: 46px; }
  .card--back .brand { left: 0; top: 22px; width: 441px; font-size: 19px; line-height: 1.1; gap: 10px; }
  .card--back .brand__dot { width: 52px; height: 52px; }

  /* front details */
  .contact { position: absolute; left: 223px; top: 40px; font-size: 12.5px; line-height: 1; }
  .contact__name { font-size: 15.5px; font-weight: 600; color: var(--navy); }
  .contact__name .first { color: var(--red); }
  .contact__role { margin-top: 3px; font-size: 12px; }
  .contact__list { list-style: none; margin-top: 16px; }
  .contact__list li { display: flex; align-items: center; gap: 6px; height: 16px; }
  .contact__list li.gap { margin-bottom: 11px; }
  .icon { width: 11px; height: 11px; flex: none; fill: var(--red); }
  .license { margin-top: 12px; color: var(--red); font-size: 12.5px; }
  .license__head { font-size: 14.5px; font-weight: 600; margin-bottom: 2px; }
  .license p { line-height: 16px; }
  .license span { color: var(--navy); }

  /* divider with centered text */
  .divider {
    position: absolute; left: 0; right: 0; top: 234px;
    display: flex; align-items: center; gap: 10px;
    font-size: 13.5px; white-space: nowrap;
  }
  .divider::before, .divider::after { content: ""; flex: 1; height: 1px; background: var(--rule); }
  .card--front .divider::before { flex: 0 0 119px; }
  .card--back .divider { top: 236px; color: var(--red); font-size: 12.5px; }
  .card--back .divider::before, .card--back .divider::after { background: var(--rule-red); }

  /* services */
  .services {
    position: absolute; left: 0; width: 441px; top: 145px;
    list-style: none; text-align: center;
    font-size: 12.5px; text-transform: uppercase; line-height: 16px;
  }
  .services li { display: flex; justify-content: center; align-items: center; gap: 6px; }
  .tick { width: 10px; height: 10px; fill: none; stroke: var(--red); stroke-width: 2.6; stroke-linecap: round; stroke-linejoin: round; }
</style>
</head>
<body>

<section class="card card--front" aria-label="Business card front">
  <div class="brand">
    <span class="brand__dot"></span>
    <span class="brand__name">Harbor Lantern Security &amp; Electric</span>
  </div>

  <div class="contact">
    <p class="contact__name"><span class="first">Marcus</span> Tremblow</p>
    <p class="contact__role">Owner</p>
    <ul class="contact__list">
      <li class="gap">
        <svg class="icon" viewBox="0 0 12 12"><path d="M6 0.5a4 4 0 0 0-4 4c0 3 4 7 4 7s4-4 4-7a4 4 0 0 0-4-4zm0 5.6a1.6 1.6 0 1 1 0-3.2 1.6 1.6 0 0 1 0 3.2z"/></svg>
        Marrowdale, Texas
      </li>
      <li>
        <svg class="icon" viewBox="0 0 12 12"><path d="M2.6 1l1.9 2.3-1 1.3c.8 1.6 2 2.8 3.6 3.6l1.3-1L10.7 9l-1 1.7C5.2 10.5 1.5 6.8 1.3 2.2z"/></svg>
        936-555-0193
      </li>
      <li>
        <svg class="icon" viewBox="0 0 12 12"><path d="M1 3h10v6.5H1z M1 3l5 3.6L11 3" stroke="#fff" stroke-width="0.9"/></svg>
        mtremblow@quillmail.example
      </li>
      <li>
        <svg class="icon" viewBox="0 0 12 12"><circle cx="6" cy="6" r="5"/><path d="M1 6h10M6 1c-2.4 2.8-2.4 7.2 0 10M6 1c2.4 2.8 2.4 7.2 0 10" stroke="#fff" stroke-width="0.8" fill="none"/></svg>
        www.yourharborlanterntx.example
      </li>
    </ul>
    <div class="license">
      <p class="license__head">Licensed and Insured</p>
      <p>License Number: <span>K47315</span></p>
      <p>TECL: <span>58629</span></p>
    </div>
  </div>

  <p class="divider">We're There When You're Not</p>
</section>

<section class="card card--back" aria-label="Business card back">
  <div class="brand">
    <span class="brand__dot"></span>
    <span class="brand__name">Harbor Lantern Security &amp; Electric</span>
  </div>

  <ul class="services">
    <li><svg class="tick" viewBox="0 0 10 10"><path d="M1.5 5.3l2.3 2.3L8.5 2.4"/></svg>Residential and Commercial Electrical Services</li>
    <li><svg class="tick" viewBox="0 0 10 10"><path d="M1.5 5.3l2.3 2.3L8.5 2.4"/></svg>Electric Gates</li>
    <li><svg class="tick" viewBox="0 0 10 10"><path d="M1.5 5.3l2.3 2.3L8.5 2.4"/></svg>Alarm Systems</li>
    <li><svg class="tick" viewBox="0 0 10 10"><path d="M1.5 5.3l2.3 2.3L8.5 2.4"/></svg>Alarm Monitoring</li>
    <li><svg class="tick" viewBox="0 0 10 10"><path d="M1.5 5.3l2.3 2.3L8.5 2.4"/></svg>Cameras</li>
  </ul>

  <p class="divider">NO JOB TOO BIG OR SMALL, WE DO IT ALL</p>
</section>

</body>
</html>
```